Delegate Welcome sign

The Copperfield Lodge hotel in Pine Bush NY is welcoming delegations from many different countries during 2019. We want to make a welcome sign about 16:9 ratio about 4 feet high with raised letters. I have attached a background design that we liked and a template with the wording. As you will see I need help with it.

```html
<!DOCTYPE html>
<html lang="en">
<head>
<meta charset="utf-8">
<title>Copperfield Lodge – Delegate Welcome Sign</title>
<link href="https://fonts.googleapis.com/css2?family=Cinzel:wght@500&family=PT+Serif:wght@400;700&family=Rye&display=swap" rel="stylesheet">
<style>
  :root {
    --page: #ffffff;
    --slate: #3c4d4d;
    --slate-deep: #2e3b3b;
    --leaf: #5f8585;
    --apricot: #f2a35e;
    --butter: #fbd27b;
    --cream: #fff7ea;
  }
  html, body {
    margin: 0;
    padding: 0;
    width: 1200px;
    height: 1000px;
    overflow: hidden;
    background: var(--page);
  }
  .canvas {
    position: relative;
    width: 1200px;
    height: 1000px;
  }
  .sign {
    position: absolute;
    left: 0;
    top: 0;
  }
  .hotel-name {
    font-family: "Cinzel", "Times New Roman", serif;
    font-weight: 500;
    font-size: 44px;
    fill: var(--cream);
  }
  .welcomes {
    font-family: "PT Serif", Georgia, serif;
    font-weight: 700;
    font-size: 54px;
    fill: var(--butter);
  }
  .headline {
    font-family: "Rye", Georgia, serif;
    font-size: 96px;
    fill: var(--butter);
    stroke: var(--slate-deep);
    stroke-width: 10px;
    stroke-linejoin: round;
    paint-order: stroke;
  }
  .destination {
    font-family: "PT Serif", Georgia, serif;
    font-weight: 700;
    font-size: 47px;
    fill: var(--butter);
    stroke: var(--slate-deep);
    stroke-width: 6px;
    stroke-linejoin: round;
    paint-order: stroke;
  }
  .hashtag {
    font-family: "PT Serif", Georgia, serif;
    font-weight: 400;
    font-size: 27px;
    fill: var(--cream);
  }
  .panel { fill: var(--slate); }
  .banner { fill: var(--apricot); }
</style>
</head>
<body>
<div class="canvas">
  <svg class="sign" width="1200" height="1000" viewBox="0 0 1200 1000" xmlns="http://www.w3.org/2000/svg">
    <defs>
      <radialGradient id="leaf-field" cx="50%" cy="50%" r="70%">
        <stop offset="0%" stop-color="#4d6767"/>
        <stop offset="100%" stop-color="#3f5454"/>
      </radialGradient>
    </defs>

    <rect class="panel" x="75" y="226" width="1055" height="594"/>
    <rect x="75" y="226" width="1055" height="594" fill="url(#leaf-field)"
          role="img" aria-label="Decorative pattern of teal leaves radiating in clustered bursts"/>

    <path class="banner" d="M218 226 H1010 L958 312 Q950 326 934 326 H292 Q276 326 268 312 Z"/>
    <text class="hotel-name" x="614" y="303" text-anchor="middle" textLength="640" lengthAdjust="spacingAndGlyphs">THE COPPERFIELD LODGE HOTEL</text>

    <text class="welcomes" x="613" y="408" text-anchor="middle">welcomes</text>

    <text class="headline" x="603" y="538" text-anchor="middle" textLength="1000" lengthAdjust="spacingAndGlyphs">2019 INTERNATIONAL</text>
    <text class="headline" x="612" y="664" text-anchor="middle" textLength="512" lengthAdjust="spacingAndGlyphs">DELEGATES</text>

    <text class="destination" x="614" y="724" text-anchor="middle" textLength="830" lengthAdjust="spacingAndGlyphs">to the Hudson Valley in New York</text>

    <path class="banner" d="M432 820 L474 784 Q481 778 490 778 H736 Q745 778 752 784 L792 820 Z"/>
    <text class="hashtag" x="612" y="808" text-anchor="middle" textLength="232" lengthAdjust="spacingAndGlyphs">#copperfieldlodgehotel</text>
  </svg>
</div>
</body>
</html>
```